IT Consulting Company needs a PowerPoint Template Design

We need a PowerPoint template design for an IT Consulting company called "Vorensik" (www.vorensik-example.com). We provide IT consulting services to customers. We mostly use the PowerPoint to present diagram, tables, lots of text. So, we would like to see the designs that is bold, modern and easy to read text. There should be the attached logo on every slides. The final design should communicate "Most Trusted IT Advisor".

Industry/Entity Type

It Company

Requirements
Must have
• The PowerPoint Template must have the following pages:
1. Title Slide (Main Title, Sub Title, Speaker, Date)
2. Title and Content (Bulleted content)
3. Title and Content (Numbered content)
4. Title and Table (Multiple columns with header and footer)
5. General Section header (Main Title, Sub Title)
6. Section header ("Demo" with graphic)
7. Section header ("Q&A" with graphic)
8. Section header ("Business Requirement" with graphic)
9. Section header ("Progress Update" with graphic)
10. Section header ("Project Plan" with graphic)
11. Closing Slide ("Thank you" with graphic)
Nice to have
• We prefer color blue. But other colors are welcome.

```html
<!DOCTYPE html>
<html lang="en">
<head>
<meta charset="utf-8">
<title>Vorensik – Presentation Template</title>
<link rel="stylesheet" href="https://fonts.googleapis.com/css2?family=PT+Sans:wght@400;700&display=swap">
<style>
  :root {
    --navy: #1f2d4e;
    --red: #d71f27;
    --red-soft: #e0575c;
    --white: #ffffff;
    --row-grey: #d4d7de;
    --frame: #8c93a3;
    --ink: #1f2d4e;
  }
  * { box-sizing: border-box; margin: 0; padding: 0; }
  html, body { width: 1200px; height: 1200px; overflow: hidden; background: var(--white); }
  body { font-family: "PT Sans", Tahoma, sans-serif; color: var(--ink); }
  .canvas { position: relative; width: 1200px; height: 1200px; overflow: hidden; background: var(--white); }

  .slide {
    position: absolute; width: 336px; height: 252px; overflow: hidden;
    border: 1px solid var(--frame); background: var(--white);
  }
  .slide--dark { background: var(--navy); }
  .slide-art { position: absolute; inset: 0; width: 100%; height: 100%; display: block; }

  .col-1 { left: 30px; } .col-2 { left: 432px; } .col-3 { left: 834px; }
  .row-1 { top: 38px; } .row-2 { top: 329px; } .row-3 { top: 619px; } .row-4 { top: 910px; }

  /* brand name */
  .brand { position: absolute; display: flex; align-items: center; gap: 6px; background: var(--white); }
  .brand-name { font-weight: 700; color: var(--navy); letter-spacing: 0.3px; }
  .brand-dot { width: 7px; height: 7px; border-radius: 50%; background: var(--red); }
  .brand--large { left: 36px; top: 196px; width: 144px; height: 44px; padding-left: 10px; }
  .brand--large .brand-name { font-size: 25px; }
  .brand--small { left: 82px; top: 211px; width: 86px; height: 29px; padding-left: 6px; gap: 4px; }
  .brand--small .brand-name { font-size: 16px; }
  .brand--small .brand-dot { width: 5px; height: 5px; }
  .brand--footer { right: 14px; bottom: 8px; background: transparent; gap: 4px; }
  .brand--footer .brand-name { font-size: 14px; }
  .brand--footer .brand-dot { width: 5px; height: 5px; }

  /* content slides */
  .header-title {
    position: absolute; left: 14px; top: 0; height: 40px; line-height: 40px;
    font-size: 11.5px; font-weight: 700; color: var(--white); text-transform: uppercase;
  }
  .body-text {
    position: absolute; left: 12px; right: 12px; top: 50px;
    font-size: 11.4px; line-height: 1.22; color: var(--navy);
  }
  .accent { color: var(--red); font-weight: 700; }
  .numbered { list-style: none; counter-reset: item; }
  .numbered li { counter-increment: item; position: relative; padding-left: 11px; margin-bottom: 4px; }
  .numbered li::before { content: counter(item) "."; position: absolute; left: 0; }

  .data-table {
    position: absolute; left: 48px; top: 56px; width: 238px;
    border-collapse: collapse; font-size: 9px; text-align: center; color: var(--navy);
  }
  .data-table th { background: var(--red); color: var(--white); font-weight: 700; height: 15px; border: 2px solid var(--white); }
  .data-table td { height: 16.5px; border-left: 2px solid var(--white); border-right: 2px solid var(--white); }
  .data-table tbody tr:nth-child(odd) td { background: var(--row-grey); }

  /* section slides */
  .section-title {
    position: absolute; left: 31px; top: 14px; color: var(--white);
    font-size: 20px; line-height: 1.15; font-weight: 400;
  }
  .section-title--caps { font-size: 20px; top: 24px; text-transform: uppercase; }
  .section-subtitle {
    position: absolute; left: 31px; top: 56px; color: var(--white);
    font-size: 11px; font-weight: 700; text-transform: uppercase;
  }
  .photo-label {
    position: absolute; color: var(--white); font-size: 11px; font-weight: 700;
  }
  .closing-title {
    position: absolute; right: 10px; top: 80px; color: var(--white);
    font-size: 54px; line-height: 0.9; text-align: right; font-weight: 400;
  }
</style>
</head>
<body>
<main class="canvas">

  <!-- 1 Title slide -->
  <section class="slide slide--dark col-1 row-1">
    <svg class="slide-art" viewBox="0 0 280 210" preserveAspectRatio="none">
      <path fill="var(--red)" d="M160 210 C120 150 140 35 245 0 L280 0 L280 210 Z"/>
    </svg>
    <div class="brand brand--large"><span class="brand-name">Vorensik</span><span class="brand-dot"></span></div>
  </section>

  <!-- 2 Title and bulleted content -->
  <section class="slide col-2 row-1">
    <svg class="slide-art" viewBox="0 0 280 210" preserveAspectRatio="none">
      <rect width="280" height="33" fill="var(--navy)"/>
      <path fill="var(--red)" d="M175 33 C190 15 215 4 245 0 L280 0 L280 33 Z"/>
      <path fill="var(--red)" d="M0 183 L143 183 C150 192 154 202 158 210 L0 210 Z"/>
    </svg>
    <h2 class="header-title">Click to add title</h2>
    <p class="body-text">Lorem ipsum dolor sit amet, consectetur adipiscing elit. Nam et dolor scelerisque, condimentum sapien id, posuere justo. <span class="accent">Interdum et malesuada</span> fames ac ante ipsum primis in faucibus. Pellentesque vel auctor mi. Class aptent taciti sociosqu ad litora torquent per conubia nostra, per inceptos himenaeos. Duis bibendum eget eros ut facilisis. Vivamus sodales nibh vel augue interdum vestibulum ut quis tellus. In vitae placerat magna. Curabitur nec feugiat lacus, et fermentum nibh.</p>
    <div class="brand brand--footer"><span class="brand-name">Vorensik</span><span class="brand-dot"></span></div>
  </section>

  <!-- 3 Title and numbered content -->
  <section class="slide col-3 row-1">
    <svg class="slide-art" viewBox="0 0 280 210" preserveAspectRatio="none">
      <rect width="280" height="33" fill="var(--navy)"/>
      <path fill="var(--red)" d="M175 33 C190 15 215 4 245 0 L280 0 L280 33 Z"/>
      <path fill="var(--red)" d="M0 183 L143 183 C150 192 154 202 158 210 L0 210 Z"/>
    </svg>
    <h2 class="header-title">Click to add title</h2>
    <ol class="body-text numbered">
      <li>Lorem ipsum dolor sit amet, consectetur adipiscing elit. Nam et dolor scelerisque, condimentum sapien id, posuere justo.</li>
      <li><span class="accent">Interdum et malesuada</span> fames ac ante ipsum primis in faucibus. Pellentesque vel auctor mi.</li>
      <li>Class aptent taciti sociosqu ad litora torquent per conubia nostra, per inceptos himenaeos.</li>
      <li>Duis bibendum eget eros ut facilisis. Vivamus sodales nibh vel augue interdum vestibulum ut quis tellus. In vitae placerat magna.</li>
    </ol>
    <div class="brand brand--footer"><span class="brand-name">Vorensik</span><span class="brand-dot"></span></div>
  </section>

  <!-- 4 Title and table -->
  <section class="slide col-1 row-2">
    <svg class="slide-art" viewBox="0 0 280 210" preserveAspectRatio="none">
      <rect width="280" height="33" fill="var(--navy)"/>
      <path fill="var(--red)" d="M175 33 C190 15 215 4 245 0 L280 0 L280 33 Z"/>
      <path fill="var(--red)" d="M0 183 L143 183 C150 192 154 202 158 210 L0 210 Z"/>
    </svg>
    <h2 class="header-title">Click to add title</h2>
    <table class="data-table">
      <thead><tr><th>Table</th><th>Table</th><th>Table</th></tr></thead>
      <tbody>
        <tr><td>2</td><td>7</td><td>12</td></tr>
        <tr><td>7</td><td>12</td><td>14</td></tr>
        <tr><td>2</td><td>7</td><td>12</td></tr>
        <tr><td>7</td><td>12</td><td>14</td></tr>
        <tr><td>2</td><td>7</td><td>12</td></tr>
        <tr><td>7</td><td>12</td><td>14</td></tr>
        <tr><td>2</td><td>7</td><td>12</td></tr>
      </tbody>
    </table>
    <div class="brand brand--footer"><span class="brand-name">Vorensik</span><span class="brand-dot"></span></div>
  </section>

  <!-- 5 General section header -->
  <section class="slide slide--dark col-2 row-2">
    <svg class="slide-art" viewBox="0 0 280 210" preserveAspectRatio="none">
      <path fill="var(--red)" d="M150 210 C125 150 140 35 240 0 L280 0 L280 210 Z"/>
    </svg>
    <h2 class="section-title section-title--caps">Click to add title</h2>
    <p class="section-subtitle">Click to add title</p>
    <div class="brand brand--small"><span class="brand-name">Vorensik</span><span class="brand-dot"></span></div>
  </section>

  <!-- 6 Business Requirement -->
  <section class="slide slide--dark col-3 row-2">
    <svg class="slide-art" viewBox="0 0 280 210" preserveAspectRatio="none">
      <defs>
        <linearGradient id="photo-br" x1="0" y1="0" x2="1" y2="1">
          <stop offset="0" stop-color="var(--red-soft)"/><stop offset="1" stop-color="var(--red)"/>
        </linearGradient>
      </defs>
      <path role="img" aria-label="Red-toned photo of a hand touching a network of cloud icons" fill="url(#photo-br)" d="M160 210 C120 150 140 35 245 0 L280 0 L280 210 Z"/>
    </svg>
    <h2 class="section-title">Business<br>Requirement</h2>
    <div class="brand brand--large"><span class="brand-name">Vorensik</span><span class="brand-dot"></span></div>
  </section>

  <!-- 7 Demo -->
  <section class="slide slide--dark col-1 row-3">
    <svg class="slide-art" viewBox="0 0 280 210" preserveAspectRatio="none">
      <defs>
        <linearGradient id="photo-demo" x1="0" y1="0" x2="1" y2="1">
          <stop offset="0" stop-color="var(--red-soft)"/><stop offset="1" stop-color="#b8232b"/>
        </linearGradient>
      </defs>
      <path role="img" aria-label="Red-toned photo of a miniature worker on a circuit board" fill="url(#photo-demo)" d="M160 210 C120 150 140 35 245 0 L280 0 L280 210 Z"/>
    </svg>
    <h2 class="section-title" style="top:24px">DEMO</h2>
    <div class="brand brand--large"><span class="brand-name">Vorensik</span><span class="brand-dot"></span></div>
  </section>

  <!-- 8 Q&A -->
  <section class="slide slide--dark col-2 row-3">
    <svg class="slide-art" viewBox="0 0 280 210" preserveAspectRatio="none">
      <defs>
        <linearGradient id="photo-qa" x1="0" y1="0" x2="1" y2="1">
          <stop offset="0" stop-color="var(--red-soft)"/><stop offset="1" stop-color="#c93a41"/>
        </linearGradient>
      </defs>
      <path role="img" aria-label="Red-toned photo of a person seen from behind under question marks" fill="url(#photo-qa)" d="M155 210 C120 150 140 35 245 0 L280 0 L280 210 Z"/>
    </svg>
    <h2 class="section-title" style="top:24px">Q&amp;A</h2>
    <p class="photo-label" style="left:206px; top:200px">Q&amp;A</p>
    <div class="brand brand--large"><span class="brand-name">Vorensik</span><span class="brand-dot"></span></div>
  </section>

  <!-- 9 Progress Update -->
  <section class="slide slide--dark col-3 row-3">
    <svg class="slide-art" viewBox="0 0 280 210" preserveAspectRatio="none">
      <defs>
        <linearGradient id="photo-pu" x1="0" y1="1" x2="1" y2="0">
          <stop offset="0" stop-color="#c42a31"/><stop offset="1" stop-color="var(--red-soft)"/>
        </linearGradient>
      </defs>
      <path role="img" aria-label="Red-toned image of binary code with a rising arrow" fill="url(#photo-pu)" d="M145 210 C128 150 132 50 160 0 L280 0 L280 210 Z"/>
    </svg>
    <h2 class="section-title" style="left:30px">Progress<br>Update</h2>
    <div class="brand brand--large"><span class="brand-name">Vorensik</span><span class="brand-dot"></span></div>
  </section>

  <!-- 10 Project Plan -->
  <section class="slide slide--dark col-1 row-4">
    <svg class="slide-art" viewBox="0 0 280 210" preserveAspectRatio="none">
      <defs>
        <linearGradient id="photo-pp" x1="0" y1="0" x2="1" y2="1">
          <stop offset="0" stop-color="var(--red-soft)"/><stop offset="1" stop-color="#c0343b"/>
        </linearGradient>
      </defs>
      <path role="img" aria-label="Red-toned photo of a businessman facing a sketched city plan" fill="url(#photo-pp)" d="M155 210 C120 150 140 35 245 0 L280 0 L280 210 Z"/>
    </svg>
    <h2 class="section-title" style="top:24px">Project Plan</h2>
    <p class="photo-label" style="left:206px; top:200px">Project Plan</p>
    <div class="brand brand--large"><span class="brand-name">Vorensik</span><span class="brand-dot"></span></div>
  </section>

  <!-- 11 Closing slide -->
  <section class="slide slide--dark col-2 row-4">
    <svg class="slide-art" viewBox="0 0 280 210" preserveAspectRatio="none">
      <path fill="var(--red)" d="M158 210 C125 150 140 35 240 0 L280 0 L280 210 Z"/>
    </svg>
    <h2 class="closing-title">Thank<br>you</h2>
    <div class="brand brand--small"><span class="brand-name">Vorensik</span><span class="brand-dot"></span></div>
  </section>

</main>
</body>
</html>
```